Nux- luxurious rental suites coming soon

Looking for a large size banner design. The banner will include the logo "NUX". The logo has already been designed by one of your designers (Pelkin). The banner is to be placed on the building fence and will be used as a marketing/ advertisement purpose to display what's coming soon. It needs to be clean and elegant since it's representing upscale apartements.
Requesting Pelkin to be one of the designers. Thanks.

Hi all-here is the logo link. Banner will be printed on 3 separate boards that will be attached side by side to look like one big one. We are doing it this way to be able to make future modifications on 1 board at a time. Each board will be 10'Wx8'H panel. Logo design needs to be in the middle board and other left and right side boards will have the info like "coming soon and building picture". For now, please use any building image, I will be sending the actual building image later on for an update. Please do not include full image of building, choose a section and zoom or crop portion of building image so it looks more interesting. Building will be a luxurious rental in downtown. Thanks. https://www.filvanta.net/sh/k4mrvtq9ws2bdhx/XJR7KW2PL_bn4QLMvhtTcs8Ey?dl=0x

Re: banner: Instead of "coming soon" please use "coming this fall'. Thanks

professionals

Residential rentals

Serif

• use wording such as: coming this fall, 1&2 bedroom suites, designer finishes, terrace views
• Banner will be placed on site over a black mesh backdrop. Please design in a way that will make it look like blending with mesh
• Banner should not be too colorf. Please use white, grey or yellow... refer to logo image

```html
<!DOCTYPE html>
<html lang="en">
<head>
<meta charset="utf-8">
<title>Nux – Coming This Fall</title>
<link href="https://fonts.googleapis.com/css2?family=Oswald:wght@300;700&family=Poppins:wght@200;400&display=swap" rel="stylesheet">
<style>
  :root {
    --black: #000000;
    --yellow: #ffcc00;
    --white: #ffffff;
    --grey: #8c8c8c;
    --grey-light: #a8a8a8;
    --interior-dark: #1a1a1a;
    --interior-mid: #3a3a3c;
    --interior-warm: #5a4630;
    --sky: #3b3f6e;
    --facade: #8a7a68;
    --brick: #6a2a22;
  }
  * { margin: 0; padding: 0; box-sizing: border-box; }
  html, body {
    width: 1200px; height: 300px; overflow: hidden; background: var(--black);
  }
  .banner {
    position: relative; width: 1200px; height: 300px; overflow: hidden;
    background: var(--black);
  }
  .interior-visual {
    position: absolute; left: 0; top: 0; width: 830px; height: 300px;
    background:
      radial-gradient(ellipse 45% 70% at 48% 50%, rgba(90,80,70,0.55), transparent 70%),
      radial-gradient(ellipse 30% 50% at 30% 30%, rgba(70,70,72,0.6), transparent 70%),
      linear-gradient(90deg, var(--interior-dark) 0%, var(--interior-mid) 35%, var(--interior-warm) 55%, var(--interior-dark) 80%, var(--black) 100%);
    opacity: 0.85;
  }
  .interior-visual::after {
    content: ""; position: absolute; inset: 0;
    background: linear-gradient(90deg, rgba(0,0,0,0.55) 0%, rgba(0,0,0,0.2) 40%, rgba(0,0,0,0.4) 70%, var(--black) 100%);
  }
  .building-visual { position: absolute; left: 0; top: 0; width: 1200px; height: 300px; }

  .features {
    position: absolute; right: 832px; top: 72px;
    text-align: right; font-family: 'Oswald', sans-serif; text-transform: uppercase;
  }
  .features__headline {
    color: var(--yellow); font-weight: 700; font-size: 37px; line-height: 40px;
    letter-spacing: 3px;
  }
  .features__item {
    color: var(--white); font-weight: 300; font-size: 37px; line-height: 39.5px;
    letter-spacing: 2px;
  }
  .divider {
    position: absolute; left: 383px; top: 77px; width: 3px; height: 147px;
    background: var(--yellow);
  }
  .address {
    position: absolute; left: 556px; top: 64px;
    font-family: 'Poppins', sans-serif; font-weight: 400; font-size: 21px;
    letter-spacing: 5px; color: var(--grey-light); text-transform: uppercase;
  }
  .brand-name {
    position: absolute; left: 414px; top: 72px;
    font-family: 'Poppins', sans-serif; font-weight: 200; font-size: 166px;
    line-height: 1; letter-spacing: 4px; color: var(--grey);
  }
  .website {
    position: absolute; left: 497px; top: 244px;
    font-family: 'Poppins', sans-serif; font-weight: 400; font-size: 21px;
    letter-spacing: 2.5px; color: var(--white);
  }
</style>
</head>
<body>
<div class="banner">
  <div class="interior-visual" role="img" aria-label="Dimly lit modern suite interior with dining table, orange chairs and a window view of the city"></div>

  <svg class="building-visual" width="1200" height="300" viewBox="0 0 1200 300">
    <defs>
      <linearGradient id="buildingTone" x1="0" y1="0" x2="0" y2="1">
        <stop offset="0" stop-color="#4a5088"/>
        <stop offset="0.3" stop-color="#7d7064"/>
        <stop offset="0.62" stop-color="#9a8a74"/>
        <stop offset="0.75" stop-color="#4d5a34"/>
        <stop offset="1" stop-color="#6a2a22"/>
      </linearGradient>
    </defs>
    <path role="img" aria-label="Evening view of the terraced residential building with lit windows and rooftop greenery"
          d="M812 0 C850 40 858 90 842 130 C826 175 820 200 828 235 C834 262 848 285 862 300 L1200 300 L1200 0 Z"
          fill="url(#buildingTone)"/>
    <path d="M810 0 C850 40 858 90 840 130 C824 175 818 200 826 235 C832 262 846 285 860 300"
          fill="none" stroke="var(--yellow)" stroke-width="6"/>
  </svg>

  <div class="features">
    <p class="features__headline">Coming This Fall</p>
    <p class="features__item">1&amp;2 Bedroom Suites</p>
    <p class="features__item">Designer Finishes</p>
    <p class="features__item">Terrace Views</p>
  </div>
  <div class="divider"></div>

  <p class="address">148 Marlowe</p>
  <h1 class="brand-name">NUX</h1>
  <p class="website">www.nuxresidences.com</p>
</div>
</body>
</html>
```